Webiste Design KDW

Design the website using uploaded content. Design colors should match that of the company logo with an allowance of one more extra color if it makes the website look much better and colorful. Use Technology related stock images in your design.

Target Market(s)

Potential Clients - Companies

Industry/Entity Type

Information Technology

Coding

Coded - Design and coding required

Number of Pages Required

5+ page

Requirements
Must have
• Company Logo Colors
Nice to have
• Professional Look and Feel with Sliders showing professional information technology images

```html
<!DOCTYPE html>
<html lang="en">
<head>
<meta charset="utf-8">
<title>KDW Technologies</title>
<link href="https://fonts.googleapis.com/css2?family=Poppins:wght@500;600;700&family=Nunito+Sans:wght@400;600;700;800&display=swap" rel="stylesheet">
<style>
:root{
  --orange:#ff8a00;
  --orange-soft:#fde8d2;
  --ink:#1d1d1f;
  --text:#444;
  --muted:#666;
  --grey-bg:#f2f1f0;
  --white:#fff;
  --dark:#0b0b0d;
  --line:#e3e3e3;
}
*{margin:0;padding:0;box-sizing:border-box}
html,body{width:1200px;height:3710px;overflow:hidden}
body{font-family:"Nunito Sans",Arial,sans-serif;color:var(--text);background:var(--white);position:relative}
h1,h2,h3,h4{font-family:"Poppins",Arial,sans-serif;color:var(--ink)}
.btn{display:inline-block;background:var(--orange);color:var(--white);font-family:"Poppins",Arial,sans-serif;font-weight:700;font-size:11px;letter-spacing:.3px;padding:7px 14px;border-radius:16px;text-decoration:none}
.rule{width:22px;height:2px;background:var(--ink);margin:18px auto 0}
.section-title{text-align:center;font-size:19px;font-weight:600;letter-spacing:.3px}
.brand{font-family:"Nunito Sans",Arial,sans-serif;font-weight:800;color:var(--orange);display:flex;align-items:center;gap:10px}
.brand .dot{width:14px;height:14px;border-radius:50%;background:var(--orange)}

.site-header{position:absolute;top:0;left:0;width:1200px;height:115px}
.site-header .brand{position:absolute;left:132px;top:32px;font-size:44px;letter-spacing:1px}
.contact-quick{position:absolute;top:22px;right:132px;display:flex;gap:30px}
.contact-quick .item{display:flex;align-items:center;gap:10px}
.contact-quick .ico{width:28px;height:28px;border-radius:50%;background:var(--orange);display:flex;align-items:center;justify-content:center}
.contact-quick small{display:block;font-size:9px;color:var(--ink);letter-spacing:.5px}
.contact-quick span{font-size:17px;color:var(--ink)}
.main-nav{position:absolute;top:74px;right:132px;display:flex;gap:42px;font-size:14px;color:var(--ink);letter-spacing:.4px}
.main-nav a{color:inherit;text-decoration:none;padding-bottom:6px}
.main-nav a.active{color:var(--orange);border-bottom:1px solid var(--orange)}

.hero{position:absolute;top:115px;left:0;width:1200px;height:469px;text-align:center;color:var(--white)}
.hero-photo{position:absolute;inset:0;background:radial-gradient(ellipse at 50% 45%,#5d7fa6 0%,#27405f 35%,#101b2c 75%,#0a111d 100%)}
.hero-content{position:relative;padding-top:78px}
.hero h1{color:var(--white);font-size:46px;font-weight:600}
.hero p{font-size:17px;line-height:24px;margin:14px auto 0;width:720px}
.hero .btn{margin-top:22px;font-size:13px;padding:10px 22px;border-radius:20px}
.slider-dots{position:absolute;bottom:33px;left:0;right:0;display:flex;justify-content:center;gap:10px}
.slider-dots i{width:8px;height:8px;border-radius:50%;background:var(--white)}
.slider-dots i.on{background:var(--orange)}

.mission-band{position:absolute;top:584px;left:0;width:1200px;height:384px;background:var(--orange);color:var(--white)}
.mv{position:absolute;top:38px;width:410px}
.mv svg{display:block;height:52px}
.mv.mission{left:163px}
.mv.vision{left:691px;width:300px}
.mv h3{color:var(--white);font-size:19px;font-weight:700;margin:16px 0 12px}
.mv p{font-size:14px;line-height:19px;margin-bottom:18px}
.mv.vision p{line-height:22px}

.services{position:absolute;top:968px;left:0;width:1200px;height:722px;background:linear-gradient(180deg,var(--white) 0%,var(--white) 40%,var(--grey-bg) 100%)}
.services .section-title{margin-top:48px}
.service-cards{position:absolute;top:137px;left:131px;display:flex;gap:28px}
.service-card{width:294px;height:375px;background:var(--white);border-radius:10px;box-shadow:0 4px 18px rgba(0,0,0,.07);text-align:center;padding-top:46px}
.service-card h4{font-size:15px;font-weight:600;line-height:22px;margin-top:22px}
.service-card p{font-size:11.5px;line-height:17px;margin:18px auto 0;width:210px;color:var(--text);height:86px}
.service-card .btn{margin-top:18px}

.welcome{position:absolute;top:1690px;left:0;width:1200px;height:390px;background:var(--grey-bg)}
.welcome-photo{position:absolute;left:131px;top:17px;width:506px;height:320px;border-radius:14px;background:linear-gradient(135deg,#b9cde2 0%,#5e7fa4 40%,#203650 80%)}
.welcome-text{position:absolute;left:689px;top:0;width:360px}
.welcome-text h3{font-size:17px;font-weight:600;letter-spacing:.4px}
.welcome-text h2{font-size:24px;font-weight:700;margin-top:4px}
.welcome-text .rule{margin:14px 0 0;width:100px;height:1px}
.welcome-text p{font-size:14px;line-height:22.5px;margin-top:26px}
.welcome-text .btn{margin-top:24px}

.governance{position:absolute;top:2080px;left:0;width:1200px;height:541px;text-align:center}
.governance .section-title{margin-top:52px}
.governance .lead{font-size:14.5px;line-height:22px;margin-top:10px}
.gov-cols{position:absolute;top:207px;left:131px;display:flex}
.gov-col{width:312px;height:255px}
.gov-col+.gov-col{border-left:1px solid var(--line);width:384px}
.gov-col .badge{width:96px;height:96px;border-radius:50%;background:var(--orange-soft);margin:0 auto;display:flex;align-items:center;justify-content:center}
.gov-col h4{font-size:15px;font-weight:600;letter-spacing:.4px;margin-top:30px}
.gov-col p{font-size:11.5px;line-height:17px;margin:18px auto 0;width:245px}

.competencies{position:absolute;top:2621px;left:0;width:1200px;height:476px;background:var(--grey-bg)}
.comp-text{position:absolute;left:132px;top:50px;width:400px}
.comp-text h2{font-size:19px;font-weight:600}
.comp-text .rule{margin:14px 0 0;width:42px}
.comp-text .lead{font-size:14.5px;line-height:21px;color:var(--ink);margin-top:18px;padding-left:3px}
.comp-list{list-style:none;margin-top:22px;padding-left:3px}
.comp-list li{font-size:14.5px;line-height:32px;display:flex;align-items:center;gap:12px}
.comp-list li::before{content:"";width:8px;height:8px;border-radius:50%;background:var(--orange)}
.comp-text .btn{margin-top:14px}
.comp-photo{position:absolute;left:553px;top:0;width:647px;height:476px;background:linear-gradient(120deg,#1d4f86 0%,#2d73b6 45%,#7bb8e6 75%,#2a5b92 100%)}

.partnership{position:absolute;top:3097px;left:0;width:1200px;height:266px}
.partnership .section-title{margin-top:56px}
.partner-row{position:absolute;top:138px;left:85px;display:flex;align-items:center;gap:12px}
.partner-row .arrow{width:34px;display:flex;justify-content:center}
.partner-badge{width:146px;height:76px;border:1px solid #d9d9d9;border-radius:10px;display:flex;align-items:center;justify-content:center}
.partner-badge i{width:84px;height:22px;border-radius:4px;background:#dfe3e8}

.site-footer{position:absolute;top:3363px;left:0;width:1200px;height:347px;background:var(--dark);border-top:4px solid var(--orange);color:var(--white)}
.site-footer .brand{position:absolute;left:132px;top:90px;font-size:46px}
.foot-col{position:absolute;top:46px}
.foot-col h5{font-family:"Nunito Sans",Arial,sans-serif;font-size:12px;font-weight:800;letter-spacing:.4px;margin-bottom:18px}
.foot-col.contact{left:504px;width:230px}
.foot-col.menu{left:790px}
.foot-col.social{left:960px}
.foot-item{display:flex;gap:12px;font-size:11.5px;line-height:15px;margin-bottom:20px}
.foot-item .ico{flex:0 0 22px;height:22px;border-radius:50%;background:var(--orange);display:flex;align-items:center;justify-content:center}
.menu a{display:block;color:var(--white);text-decoration:none;font-size:11.5px;line-height:24px}
.copyright{position:absolute;left:504px;top:295px;font-size:11px}
</style>
</head>
<body>

<header class="site-header">
  <div class="brand"><span class="dot"></span>KDW</div>
  <div class="contact-quick">
    <div class="item">
      <div class="ico"><svg width="14" height="14" viewBox="0 0 14 14"><rect x="1.5" y="3" width="11" height="8" rx="1" fill="none" stroke="#fff" stroke-width="1.4"/><path d="M2 3.5l5 4 5-4" fill="none" stroke="#fff" stroke-width="1.4"/></svg></div>
      <div><small>EMAIL US</small><span>info@kdwtech.example</span></div>
    </div>
    <div class="item">
      <div class="ico"><svg width="14" height="14" viewBox="0 0 14 14"><path d="M3 1.5l2.5 2.5-1.5 1.7c.8 1.7 2 2.9 3.6 3.7L9.3 8 12 10.5 10.7 12.3C6 12 2 8 1.7 3.1z" fill="#fff"/></svg></div>
      <div><small>CALL US</small><span>010 555 0142</span></div>
    </div>
  </div>
  <nav class="main-nav">
    <a href="#" class="active">HOME</a><a href="#">ABOUT US</a><a href="#">SERVICES</a><a href="#">INDUSTRIES</a><a href="#">CONTACT US</a>
  </nav>
</header>

<section class="hero">
  <div class="hero-photo" role="img" aria-label="Photo of a data centre aisle lined with glowing server racks"></div>
  <div class="hero-content">
    <h1>Hosting Services</h1>
    <p>We are well equipped to offer the broadest range of hosted applications and services, combining our unique experience in managing Hosting Solution services. W</p>
    <a href="#" class="btn">READ MORE</a>
  </div>
  <div class="slider-dots"><i></i><i></i><i class="on"></i><i></i><i></i></div>
</section>

<section class="mission-band">
  <div class="mv mission">
    <svg width="52" height="52" viewBox="0 0 52 52"><circle cx="24" cy="28" r="20" fill="none" stroke="#fff" stroke-width="4"/><circle cx="24" cy="28" r="11" fill="none" stroke="#fff" stroke-width="4"/><circle cx="24" cy="28" r="3.5" fill="#fff"/><path d="M25 27L44 8M38 6l6 2 2 6" fill="none" stroke="#fff" stroke-width="3.5" stroke-linecap="round"/></svg>
    <h3>MISSION</h3>
    <p>To provide and run ICT as well as Engineering solutions and services that allows our customers to focus on achieving their business objectives.</p>
    <p>We will take care of your technology issues so that you can focus on running and growing your business. Our goal is to increase the productivity, efficiency, and net profits of your company by replacing or collaborating with your existing IT staff to provide a secure, reliable, and stable technology environment.</p>
  </div>
  <div class="mv vision">
    <svg width="52" height="52" viewBox="0 0 52 52"><path d="M3 30c6-9 14-14 23-14s17 5 23 14c-6 9-14 14-23 14S9 39 3 30z" fill="none" stroke="#fff" stroke-width="3"/><circle cx="26" cy="30" r="7" fill="none" stroke="#fff" stroke-width="3"/><path d="M26 6v5M14 9l2 4M38 9l-2 4" stroke="#fff" stroke-width="3" stroke-linecap="round"/></svg>
    <h3>VISION</h3>
    <p>Our vision is to be the most innovative and preferred ICT and Engineering Company. We therefore intend to grow the business locally and internationally.</p>
  </div>
</section>

<section class="services">
  <h2 class="section-title">OUR SERVICES</h2>
  <div class="rule"></div>
  <div class="service-cards">
    <article class="service-card">
      <svg width="66" height="62" viewBox="0 0 66 62"><g fill="none" stroke="#ff8a00" stroke-width="3"><polygon points="33,8 55,20 55,42 33,54 11,42 11,20"/><path d="M33 8v46M11 20l44 22M55 20L11 42"/></g><g fill="#ff8a00"><circle cx="33" cy="8" r="6"/><circle cx="55" cy="20" r="6"/><circle cx="55" cy="42" r="6"/><circle cx="33" cy="54" r="6"/><circle cx="11" cy="42" r="6"/><circle cx="11" cy="20" r="6"/></g></svg>
      <h4>Infrastructure<br>Solutions</h4>
      <p>KDW Technologies has a strong team certified and dedicated resources, both office-based as well as site-based at customer locations spread across the country.</p>
      <a href="#" class="btn">READ MORE</a>
    </article>
    <article class="service-card">
      <svg width="66" height="62" viewBox="0 0 66 62"><circle cx="33" cy="31" r="28" fill="#ff8a00"/><g fill="#fff"><path d="M18 18c6-2 10 2 9 7s-7 5-9 11c-3-6-4-13 0-18z"/><path d="M38 10c8 2 14 8 16 16-5-2-9 1-13-3s-5-8-3-13z"/><path d="M36 40c5-3 11-2 14 2-3 6-9 10-15 11 2-4-2-9 1-13z"/></g></svg>
      <h4>Converged<br>Communication</h4>
      <p>Converged Communication Systems provides best-in-class IP Telephony / Unified Communications solutions, and delivers pro-active support services for businesses of all sizes.</p>
      <a href="#" class="btn">READ MORE</a>
    </article>
    <article class="service-card">
      <svg width="66" height="62" viewBox="0 0 66 62"><g fill="none" stroke="#ff8a00" stroke-width="3"><rect x="18" y="4" width="30" height="16"/><rect x="7" y="20" width="52" height="24" rx="3"/><rect x="17" y="36" width="32" height="22"/><path d="M22 44h22M22 50h22"/></g><circle cx="15" cy="28" r="2" fill="#ff8a00"/><circle cx="21" cy="28" r="2" fill="#ff8a00"/></svg>
      <h4>Managed<br>Print Services</h4>
      <p>KDW Technologies partnership with global leaders Printwell, Kovana, Tosara, Lexon and Hepta give our customers complete peace of mind</p>
      <a href="#" class="btn">READ MORE</a>
    </article>
  </div>
</section>

<section class="welcome">
  <div class="welcome-photo" role="img" aria-label="Photo of a businessman touching a glowing network of technology icons"></div>
  <div class="welcome-text">
    <h3>WELCOME TO</h3>
    <h2>KDW TECHNOLOGIES</h2>
    <div class="rule"></div>
    <p>KDW Technologies was founded in 2013 as a Private Company. For Most of its initial existence, the company intends to establish close relationships with its various clients, with the intension of expanding throughout South Africa. KDW Technologies is dedicated to leveraging emerging technologies to provide the highest level of quality products and services, customer service, and security.</p>
    <a href="#" class="btn">READ MORE</a>
  </div>
</section>

<section class="governance">
  <h2 class="section-title">GOVERNANCE, RISK AND ETHICS</h2>
  <p class="lead">KDW Technologies understands investor concerns and issues of governance;<br>ethics and sustainability which are also high on our agenda.</p>
  <div class="rule"></div>
  <div class="gov-cols">
    <div class="gov-col">
      <div class="badge"><svg width="52" height="52" viewBox="0 0 52 52"><g fill="none" stroke="#ff8a00" stroke-width="3" stroke-linecap="round"><circle cx="26" cy="18" r="8"/><path d="M4 28l8 14h10M48 28l-8 14H30M12 42l-3 6M40 42l3 6"/></g><circle cx="26" cy="18" r="3" fill="#ff8a00"/></svg></div>
      <h4>INTEGRITY</h4>
      <p>We believe that all decisions are made with integrity, being honest with self and with others.</p>
    </div>
    <div class="gov-col">
      <div class="badge"><svg width="52" height="52" viewBox="0 0 52 52"><path d="M10 10l7 7-4 5c3 6 7 10 13 13l5-4 7 7-5 5C20 42 10 32 6 16z" fill="none" stroke="#ff8a00" stroke-width="3" stroke-linejoin="round"/><rect x="28" y="6" width="20" height="14" rx="3" fill="#ff8a00"/><path d="M32 11h12M32 15h8" stroke="#fff" stroke-width="2"/></svg></div>
      <h4>CUSTOMER SERVICE</h4>
      <p>We believe that customers can and will take notice of and appreciate great, caring service. We base our efforts on this foundation.</p>
    </div>
    <div class="gov-col">
      <div class="badge"><svg width="52" height="52" viewBox="0 0 52 52"><g fill="#ff8a00"><rect x="12" y="32" width="6" height="12"/><rect x="22" y="26" width="6" height="18"/><rect x="32" y="20" width="6" height="24"/></g><path d="M10 26l10-8 8 5 14-12M36 11h6v6" fill="none" stroke="#ff8a00" stroke-width="3" stroke-linecap="round"/><circle cx="26" cy="26" r="22" fill="none" stroke="#ff8a00" stroke-width="2"/></svg></div>
      <h4>CONTINUOUS IMPROVEMENT</h4>
      <p>We believe in not accepting the status quo; we believe in the value of ongoing training in any form. We believe in providing opportunity for personal, professional, and organizational growth and innovation for our people and our company.</p>
    </div>
  </div>
</section>

<section class="competencies">
  <div class="comp-text">
    <h2>OUR COMPETENCIES AND CAPACITY</h2>
    <div class="rule"></div>
    <p class="lead">Our company possess years of ICT experience<br>in varied fields such as:</p>
    <ul class="comp-list">
      <li>ICT Company Setup and Management</li>
      <li>ICT Infrastructure Built and Support</li>
      <li>Hosted Environments</li>
      <li>Applications Development and Maintenance</li>
      <li>Network Deployment and Support</li>
      <li>Managed Services and Software Sales and Support</li>
      <li>Audio Visual Solutions</li>
    </ul>
    <a href="#" class="btn">READ MORE</a>
  </div>
  <div class="comp-photo" role="img" aria-label="Photo of hands typing on a laptop with floating cloud upload and file icons"></div>
</section>

<section class="partnership">
  <h2 class="section-title">PARTNERSHIP</h2>
  <div class="rule"></div>
  <div class="partner-row">
    <span class="arrow"><svg width="10" height="16" viewBox="0 0 10 16"><path d="M8 2L2 8l6 6" fill="none" stroke="#333" stroke-width="1.5"/></svg></span>
    <div class="partner-badge"><i></i></div>
    <div class="partner-badge"><i></i></div>
    <div class="partner-badge"><i></i></div>
    <div class="partner-badge"><i></i></div>
    <div class="partner-badge"><i></i></div>
    <div class="partner-badge"><i></i></div>
    <span class="arrow"><svg width="10" height="16" viewBox="0 0 10 16"><path d="M2 2l6 6-6 6" fill="none" stroke="#333" stroke-width="1.5"/></svg></span>
  </div>
</section>

<footer class="site-footer">
  <div class="brand"><span class="dot"></span>KDW</div>
  <div class="foot-col contact">
    <h5>CONTACT</h5>
    <div class="foot-item"><span class="ico"><svg width="10" height="12" viewBox="0 0 10 12"><path d="M5 11S1 7 1 4.5a4 4 0 018 0C9 7 5 11 5 11z" fill="#fff"/><circle cx="5" cy="4.5" r="1.5" fill="#ff8a00"/></svg></span><span>Unit 4, 18 Oakridge Lane<br>Halfway Park, Midrand 1685</span></div>
    <div class="foot-item"><span class="ico"><svg width="11" height="11" viewBox="0 0 14 14"><path d="M3 1.5l2.5 2.5-1.5 1.7c.8 1.7 2 2.9 3.6 3.7L9.3 8 12 10.5 10.7 12.3C6 12 2 8 1.7 3.1z" fill="#fff"/></svg></span><span>Call Us<br>010 555 0142</span></div>
    <div class="foot-item"><span class="ico"><svg width="11" height="11" viewBox="0 0 14 14"><rect x="1.5" y="3" width="11" height="8" rx="1" fill="none" stroke="#fff" stroke-width="1.6"/><path d="M2 3.5l5 4 5-4" fill="none" stroke="#fff" stroke-width="1.6"/></svg></span><span>E mail Us<br>info@kdwtech.example</span></div>
  </div>
  <nav class="foot-col menu">
    <h5>MENU</h5>
    <a href="#">HOME</a><a href="#">ABOUT US</a><a href="#">SERVICES</a><a href="#">INDUSTRIES</a><a href="#">CONTACT US</a>
  </nav>
  <div class="foot-col social">
    <h5>VOLG ONS</h5>
    <div class="foot-item"><span class="ico"></span><span>Vind ons leuk op<br>CIRCLEPAGE</span></div>
    <div class="foot-item"><span class="ico"></span><span>Volg ons op<br>BUZZLINE</span></div>
    <div class="foot-item"><span class="ico"></span><span>Volg ons op<br>WORKWEAVE</span></div>
  </div>
  <p class="copyright">Copyright © 2023 All Rights Reserved</p>
</footer>

</body>
</html>
```